Website Design for new Custom Homebuilder company R Calloway Homes

We need a website design for a new company based out of Liberty Hill, Texas called R Calloway Homes. We specialize in building unique, high end custom homes in Liberty Hill, Texas and the surrounding area. We would like to see designs that use the color black, white, copper and gold. Website needs to have a modern feel and the pages that have information about the company and then pages that have a gallery with pictures of completed homes and a page that has information on available homes.

```html
<!DOCTYPE html>
<html lang="en">
<head>
<meta charset="utf-8">
<title>R Calloway Homes</title>
<link href="https://fonts.googleapis.com/css2?family=Oswald:wght@300;400;500;600;700&family=Mulish:wght@400;600;700&display=swap" rel="stylesheet">
<style>
:root{
  --copper:#d49d69;
  --copper-deep:#a8764a;
  --black:#000;
  --ink:#161616;
  --night:#1b1b1b;
  --charcoal:#2b2b2b;
  --slate:#333333;
  --white:#fff;
  --mist:#e4e4e4;
  --muted:#8a8a8a;
}
*{margin:0;padding:0;box-sizing:border-box}
html,body{width:1200px;height:4190px;overflow:hidden;background:var(--charcoal)}
body{position:relative;font-family:'Mulish',sans-serif;color:var(--white)}
.abs{position:absolute}
.heading{font-family:'Oswald',sans-serif;font-weight:300;font-size:46px;letter-spacing:3px;text-transform:uppercase;text-align:center;color:var(--white)}
.heading span{color:var(--copper)}
.btn{position:absolute;background:var(--copper);color:#1a1a1a;font-family:'Oswald',sans-serif;font-weight:500;font-size:13px;letter-spacing:1.5px;display:flex;align-items:center;justify-content:center;text-transform:uppercase}

/* header */
.topbar{left:382px;top:0;width:818px;height:42px;background:#111;font-family:'Oswald',sans-serif;font-weight:300;font-size:13px;color:var(--copper)}
.topbar .addr{position:absolute;left:65px;top:12px}
.topbar .tel{position:absolute;right:90px;top:12px}
.navbar{left:382px;top:42px;width:818px;height:65px;background:#1c1c1c;font-family:'Oswald',sans-serif;font-weight:500;font-size:13px}
.navbar a{color:var(--white);text-decoration:none;position:absolute;top:24px}
.navbar a.active{color:var(--copper)}
.navbar .listing{top:14px;left:553px;width:110px;height:38px}
.logo-box{left:0;top:0;width:382px;height:150px;background:var(--mist);display:flex;flex-direction:column;align-items:center;justify-content:center}
.brand{font-family:'Oswald',sans-serif;font-weight:400;letter-spacing:8px;text-transform:uppercase;text-align:center}
.logo-box .brand{color:#222;font-size:20px;line-height:1.3}
.mark-square{width:16px;height:16px;border:2px solid var(--copper-deep);margin-bottom:10px}

/* hero */
.rail{left:0;top:150px;width:176px;height:486px;background:var(--black)}
.rail .line{position:absolute;left:126px;top:53px;width:2px;height:236px;background:#ddd}
.social{position:absolute;left:111px;width:32px;height:32px;border-radius:50%;background:var(--white)}
.hero-photo{left:176px;top:107px;width:1024px;height:529px;background:linear-gradient(180deg,#9fc3e0 0%,#c9d7df 40%,#b9bcbc 62%,#5f7a45 82%,#3f5a2c 100%)}
.hero-card{left:236px;top:242px;width:509px;height:301px;background:rgba(255,255,255,.55)}
.hero-card h1{position:absolute;left:48px;top:52px;font-family:'Oswald',sans-serif;font-weight:500;font-size:46px;line-height:50px;color:#111;letter-spacing:.5px}
.hero-card p{position:absolute;left:50px;top:165px;font-size:16px;color:#222}
.dots{display:flex;gap:8px}
.dots i{width:10px;height:10px;border-radius:50%;background:var(--white);display:block}
.dots i.on{background:var(--copper)}

/* about */
.about{left:0;top:636px;width:1200px;height:491px;background:var(--charcoal)}
.about h2{position:absolute;left:158px;top:88px;font-family:'Oswald',sans-serif;font-weight:300;font-size:46px;letter-spacing:3px}
.about h2 span{color:var(--copper)}
.about p{position:absolute;left:158px;width:390px;font-size:13px;line-height:20px;color:#e6e6e6}
.about .frame{position:absolute;left:592px;top:97px;width:423px;height:321px;border:2px solid #555}
.about .photo{position:absolute;left:623px;top:75px;width:419px;height:317px;background:linear-gradient(135deg,#f1f2f3,#d6dadd)}

/* projects */
.projects{left:0;top:1127px;width:1200px;height:515px;background:var(--night)}
.project-photo{position:absolute;top:128px;width:392px;height:287px}

/* homes */
.homes{left:0;top:1642px;width:1200px;height:569px;background:var(--slate)}
.card{position:absolute;top:156px;width:210px;height:332px;background:var(--white);color:#222}
.card .photo{height:205px}
.card h3{font-size:14px;font-weight:600;line-height:19px;margin:12px 11px 0}
.card .sub{font-size:12px;color:var(--copper-deep);margin:0 11px}
.card .price{font-size:14px;font-weight:600;margin:12px 11px 0}
.card .view{position:absolute;left:11px;top:302px;width:64px;height:20px;font-size:11px}
.arrow{position:absolute;width:20px;height:30px}

/* testimonials */
.testi{left:0;top:2211px;width:1200px;height:469px;background:var(--charcoal)}
.quote{position:absolute;top:143px;width:281px;height:241px;background:var(--white);color:#222}
.quote .q{position:absolute;left:24px;top:18px;font-family:'Oswald',sans-serif;font-size:30px;font-weight:700;color:#333}
.quote .qc{position:absolute;right:44px;top:100px;font-family:'Oswald',sans-serif;font-size:30px;font-weight:700;color:#333}
.quote p{position:absolute;left:24px;top:50px;width:230px;font-size:13px;line-height:22px}
.quote .avatar{position:absolute;left:24px;top:162px;width:56px;height:56px;border-radius:50%;background:linear-gradient(#bfbfbf,#666)}
.quote .name{position:absolute;left:94px;top:172px;font-size:15px}
.quote .role{position:absolute;left:94px;top:194px;font-size:12px;color:var(--muted)}
.quote .tail{position:absolute;left:36px;bottom:-16px;width:0;height:0;border-left:24px solid transparent;border-top:16px solid var(--white);transform:scaleX(-1)}

/* cta */
.cta{left:0;top:2680px;width:1200px;height:395px;background:radial-gradient(circle at 40% 40%,#b07d4f,#9c6c40)}
.cta h2{position:absolute;left:0;width:1200px;top:98px;text-align:center;font-family:'Oswald',sans-serif;font-weight:600;font-size:46px;letter-spacing:5px}
.cta p{position:absolute;left:260px;width:680px;top:177px;text-align:center;font-size:13px;line-height:20px}
.cta .dark{position:absolute;left:524px;top:240px;width:151px;height:47px;background:var(--night);color:var(--white)}

/* contact form */
.touch{left:0;top:2992px;width:605px;height:449px;background:var(--ink)}
.touch h2{position:absolute;left:158px;top:68px;font-family:'Oswald',sans-serif;font-weight:600;font-size:44px;letter-spacing:4px}
.field{position:absolute;background:var(--white);color:#333;font-size:13px;padding:14px 8px}
.map{left:605px;top:3075px;width:595px;height:366px;background:linear-gradient(135deg,#ece9e3,#dcdfe3)}

/* info */
.info{left:0;top:3441px;width:1200px;height:315px;background:var(--charcoal)}
.info .divider{position:absolute;top:0;width:1px;height:315px;background:#555}
.info .icon{position:absolute;top:126px;width:46px;height:46px;border-radius:50%;background:var(--copper);display:flex;align-items:center;justify-content:center}
.info .label{position:absolute;top:128px;font-family:'Oswald',sans-serif;font-weight:300;font-size:19px}
.info .value{position:absolute;top:160px;font-family:'Oswald',sans-serif;font-weight:500;font-size:21px;white-space:nowrap}

/* footer */
.footer{left:0;top:3756px;width:1200px;height:434px;background:#111}
.footer h4{position:absolute;top:94px;font-family:'Oswald',sans-serif;font-weight:500;font-size:17px;letter-spacing:3px;color:var(--copper)}
.footer .links a{position:absolute;left:395px;font-size:13px;color:var(--white);text-decoration:none}
.footer .links a::before{content:"";display:inline-block;width:14px;height:1px;background:#ccc;vertical-align:middle;margin-right:18px}
.footer .brand{color:var(--white);font-size:15px;letter-spacing:7px;line-height:1.4}
.insta{position:absolute;width:56px;height:53px;background:linear-gradient(#6f8fb3,#8e7e6c)}
.copyright{position:absolute;left:0;width:1200px;top:368px;text-align:center;font-size:12px}
.copyright span{color:var(--copper)}
</style>
</head>
<body>

<!-- header -->
<div class="abs logo-box">
  <div class="mark-square"></div>
  <div class="brand">R Calloway<br>Homes</div>
</div>
<div class="abs topbar">
  <svg class="abs" style="left:44px;top:13px" width="10" height="14" viewBox="0 0 10 14"><path d="M5 0a5 5 0 0 1 5 5c0 4-5 9-5 9S0 9 0 5a5 5 0 0 1 5-5z" fill="#d49d69"/><circle cx="5" cy="5" r="2" fill="#111"/></svg>
  <div class="addr">OAKMONT LANE, LIBERTY HILL, 78642</div>
  <svg class="abs" style="right:198px;top:14px" width="12" height="12" viewBox="0 0 24 24"><path d="M6.6 10.8a15 15 0 0 0 6.6 6.6l2.2-2.2c.3-.3.7-.4 1-.2 1.1.4 2.3.6 3.6.6.6 0 1 .4 1 1V20c0 .6-.4 1-1 1C10.6 21 3 13.4 3 4c0-.6.4-1 1-1h3.5c.6 0 1 .4 1 1 0 1.3.2 2.5.6 3.6.1.3 0 .7-.2 1z" fill="#d49d69"/></svg>
  <div class="tel">0 - 512 - 555 014</div>
</div>
<nav class="abs navbar">
  <a class="active" style="left:66px">HOME</a>
  <a style="left:159px">ABOUT</a>
  <a style="left:258px">GALLERY</a>
  <a style="left:368px">BLOG</a>
  <a style="left:459px">CONTACT</a>
  <div class="btn listing" style="border:2px solid #1c1c1c;outline:1px solid var(--copper)">VIEW LISTING</div>
</nav>

<!-- hero -->
<div class="abs hero-photo" role="img" aria-label="Photo of a grey two-storey house with a white porch and green lawn"></div>
<div class="abs rail">
  <div class="line"></div>
  <div class="social" style="top:309px" aria-label="Social link"></div>
  <div class="social" style="top:353px" aria-label="Social link"></div>
  <div class="social" style="top:397px" aria-label="Social link"></div>
  <div class="social" style="top:441px" aria-label="Social link"></div>
</div>
<div class="abs hero-card">
  <h1>BUILD MODERN HOUSE<br>WITH US</h1>
  <p>Lorem Ipsum is simply dummy text of the printing</p>
  <div class="btn" style="left:50px;top:208px;width:107px;height:35px">CONTACT US</div>
</div>
<div class="abs dots" style="left:575px;top:598px"><i></i><i class="on"></i><i></i></div>

<!-- about -->
<section class="abs about">
  <h2>ABOUT R <span>CALLOWAY</span></h2>
  <p style="top:165px">Lorem Ipsum is simply dummy text of the printing and typesetting industry. Lorem Ipsum has been the industry's standard dummy text ever since the 1500s.</p>
  <p style="top:243px">It is a long established fact that a reader will be distracted by the readable content .</p>
  <p style="top:297px">There are many variations of passages of Lorem Ipsum available, but the majority have suffered .</p>
  <div class="btn" style="left:158px;top:359px;width:108px;height:36px">READ MORE</div>
  <div class="frame"></div>
  <div class="photo" role="img" aria-label="Faded photo of a white modern building"></div>
</section>

<!-- projects -->
<section class="abs projects">
  <div class="heading abs" style="left:0;width:1200px;top:50px">OUR <span>PROJECTS</span></div>
  <div class="project-photo" style="left:180px;background:linear-gradient(#3f8fe0,#cfd6dc 55%,#5f8a3e 85%,#4a6e30)" role="img" aria-label="Photo of a grey shingle house with a wraparound porch"></div>
  <div class="project-photo" style="left:628px;background:linear-gradient(#2f86e6,#a04a3e 50%,#4f7a32 85%,#3d5f28)" role="img" aria-label="Photo of a red two-storey house"></div>
  <div class="abs dots" style="left:575px;top:453px"><i></i><i class="on"></i><i></i></div>
</section>

<!-- available homes -->
<section class="abs homes">
  <div class="heading abs" style="left:0;width:1200px;top:65px">AVAILABLE <span>HOMES</span></div>
  <svg class="arrow" style="left:124px;top:296px" viewBox="0 0 20 30"><path d="M15 3 4 15l11 12" fill="none" stroke="#fff" stroke-width="3"/></svg>
  <svg class="arrow" style="left:1056px;top:296px" viewBox="0 0 20 30"><path d="M5 3l11 12L5 27" fill="none" stroke="#fff" stroke-width="3"/></svg>
  <div class="card" style="left:158px">
    <div class="photo" role="img" aria-label="Photo of a grey house with a garage" style="background:linear-gradient(#4e93dc,#b8b8b4 60%,#6d8d4a)"></div>
    <h3>Lorem Ipsum is simply dummy text</h3><div class="sub">long established fact</div>
    <div class="price">$ 2.5 - $ 1.78</div><div class="btn view">VIEW</div>
  </div>
  <div class="card" style="left:383px">
    <div class="photo" role="img" aria-label="Photo of a red two-storey house" style="background:linear-gradient(#3a8ae0,#a24b40 55%,#567d36)"></div>
    <h3>Lorem Ipsum is simply dummy text</h3><div class="sub">long established fact</div>
    <div class="price">$ 2.5 - $ 1.78</div><div class="btn view">VIEW</div>
  </div>
  <div class="card" style="left:606px">
    <div class="photo" role="img" aria-label="Photo of a grey house with a white porch" style="background:linear-gradient(#5a9be0,#c9cbcb 55%,#5f8c3a)"></div>
    <h3>Lorem Ipsum is simply dummy text</h3><div class="sub">long established fact</div>
    <div class="price">$ 2.5 - $ 1.78</div><div class="btn view">VIEW</div>
  </div>
  <div class="card" style="left:832px">
    <div class="photo" role="img" aria-label="Photo of a cream Victorian house" style="background:linear-gradient(#3f88de,#d8cfae 55%,#6a8a3c)"></div>
    <h3>Lorem Ipsum is simply dummy text</h3><div class="sub">long established fact</div>
    <div class="price">$ 2.5 - $ 1.78</div><div class="btn view">VIEW</div>
  </div>
</section>

<!-- testimonials -->
<section class="abs testi">
  <div class="heading abs" style="left:0;width:1200px;top:66px">CLIENT <span>TESTIMONIAL</span></div>
  <svg class="arrow" style="left:126px;top:255px" viewBox="0 0 20 30"><path d="M15 3 4 15l11 12" fill="none" stroke="#fff" stroke-width="3"/></svg>
  <svg class="arrow" style="left:1058px;top:255px" viewBox="0 0 20 30"><path d="M5 3l11 12L5 27" fill="none" stroke="#fff" stroke-width="3"/></svg>
  <div class="quote" style="left:158px"><div class="q">&ldquo;</div><p>There are many variations of passages of Lorem Ipsum available, but the majority have suffered alteration in some form .</p><div class="qc">&rdquo;</div><div class="avatar" role="img" aria-label="Client portrait"></div><div class="name">Dana Whitfield</div><div class="role">CEO at loremipsum</div><div class="tail"></div></div>
  <div class="quote" style="left:460px"><div class="q">&ldquo;</div><p>There are many variations of passages of Lorem Ipsum available, but the majority have suffered alteration in some form .</p><div class="qc">&rdquo;</div><div class="avatar" role="img" aria-label="Client portrait"></div><div class="name">Dana Whitfield</div><div class="role">CEO at loremipsum</div><div class="tail"></div></div>
  <div class="quote" style="left:762px"><div class="q">&ldquo;</div><p>There are many variations of passages of Lorem Ipsum available, but the majority have suffered alteration in some form .</p><div class="qc">&rdquo;</div><div class="avatar" role="img" aria-label="Client portrait"></div><div class="name">Dana Whitfield</div><div class="role">CEO at loremipsum</div><div class="tail"></div></div>
</section>

<!-- call to action -->
<section class="abs cta">
  <h2>DESIGN YOUR CUSTOM HOME</h2>
  <p>Lorem Ipsum is simply dummy text of the printing and typesetting industry. Lorem Ipsum has been the industry's standard dummy text ever since the 1500s.</p>
  <div class="btn dark">CONTACT US NOW</div>
</section>

<!-- get in touch -->
<section class="abs touch">
  <h2>GET IN TOUCH</h2>
  <div class="field" style="left:158px;top:133px;width:208px;height:46px">First Name</div>
  <div class="field" style="left:376px;top:133px;width:206px;height:46px">Last Name</div>
  <div class="field" style="left:158px;top:187px;width:208px;height:46px">Email Address</div>
  <div class="field" style="left:376px;top:187px;width:206px;height:46px">Phone No</div>
  <div class="field" style="left:158px;top:241px;width:424px;height:81px;padding-top:10px">Message</div>
  <div class="btn" style="left:158px;top:333px;width:106px;height:34px">SUBMIT NOW</div>
</section>
<div class="abs map" role="img" aria-label="Street map of the office neighbourhood"></div>

<!-- contact info -->
<section class="abs info">
  <div class="divider" style="left:426px"></div>
  <div class="divider" style="left:758px"></div>
  <div class="icon" style="left:159px"><svg width="22" height="22" viewBox="0 0 24 24"><path d="M6.6 10.8a15 15 0 0 0 6.6 6.6l2.2-2.2c.3-.3.7-.4 1-.2 1.1.4 2.3.6 3.6.6.6 0 1 .4 1 1V20c0 .6-.4 1-1 1C10.6 21 3 13.4 3 4c0-.6.4-1 1-1h3.5c.6 0 1 .4 1 1 0 1.3.2 2.5.6 3.6.1.3 0 .7-.2 1z" fill="#fff"/></svg></div>
  <div class="label" style="left:225px">PHONE</div>
  <div class="value" style="left:225px">+1-512-555-0148</div>
  <div class="icon" style="left:462px"><svg width="22" height="16" viewBox="0 0 22 16"><rect x="1" y="1" width="20" height="14" rx="1" fill="none" stroke="#fff" stroke-width="2"/><path d="M1 2l10 7 10-7" fill="none" stroke="#fff" stroke-width="2"/></svg></div>
  <div class="label" style="left:527px">EMAIL</div>
  <div class="value" style="left:527px">HELLO@RCALLOWAY.COM</div>
  <div class="icon" style="left:795px"><svg width="16" height="22" viewBox="0 0 10 14"><path d="M5 0a5 5 0 0 1 5 5c0 4-5 9-5 9S0 9 0 5a5 5 0 0 1 5-5z" fill="#fff"/><circle cx="5" cy="5" r="2" fill="#d49d69"/></svg></div>
  <div class="label" style="left:862px">LOCATION</div>
  <div class="value" style="left:862px">48 RIDGEVIEW DR, &nbsp;TEXAS</div>
</section>

<!-- footer -->
<footer class="abs footer">
  <div class="abs" style="left:140px;top:155px;width:210px;display:flex;flex-direction:column;align-items:center">
    <div class="brand">R Calloway<br>Homes</div>
    <div style="display:flex;gap:6px;margin-top:14px">
      <i style="width:24px;height:24px;border-radius:50%;background:#fff;display:block" aria-label="Social link"></i>
      <i style="width:24px;height:24px;border-radius:50%;background:#fff;display:block" aria-label="Social link"></i>
      <i style="width:24px;height:24px;border-radius:50%;background:#fff;display:block" aria-label="Social link"></i>
      <i style="width:24px;height:24px;border-radius:50%;background:#fff;display:block" aria-label="Social link"></i>
    </div>
  </div>
  <h4 style="left:395px">QUICK LINK</h4>
  <div class="links">
    <a style="top:137px">Home</a><a style="top:163px">About</a><a style="top:189px">Services</a>
    <a style="top:216px">Gallery</a><a style="top:242px">Blog</a><a style="top:268px">Contact</a>
  </div>
  <h4 style="left:579px">NEWSLETTER</h4>
  <div class="abs" style="left:579px;top:134px;width:230px;font-size:12px;line-height:19px">It is a long established fact that a reader will be</div>
  <div class="field" style="left:579px;top:189px;width:227px;height:47px;font-size:12px;padding:15px 11px">Enter Your Mail Id</div>
  <div class="btn" style="left:579px;top:244px;width:107px;height:32px;font-size:12px">SUBSCRIBE</div>
  <h4 style="left:863px">INSTAGRAM</h4>
  <div class="insta" style="left:866px;top:140px" role="img" aria-label="Home photo"></div>
  <div class="insta" style="left:926px;top:140px;background:linear-gradient(#3a6fb8,#9b5a4a)" role="img" aria-label="Home photo"></div>
  <div class="insta" style="left:986px;top:140px;background:linear-gradient(#4b8ed4,#c5b48a)" role="img" aria-label="Home photo"></div>
  <div class="insta" style="left:866px;top:196px;background:linear-gradient(#6b8fb6,#8c8c8c)" role="img" aria-label="Home photo"></div>
  <div class="insta" style="left:926px;top:196px;background:linear-gradient(#3b86dd,#a54a3e)" role="img" aria-label="Home photo"></div>
  <div class="insta" style="left:986px;top:196px;background:linear-gradient(#5c9ee0,#bfc3c4)" role="img" aria-label="Home photo"></div>
  <div class="insta" style="left:866px;top:252px;background:linear-gradient(#4f7fbf,#b76b4a)" role="img" aria-label="Home photo"></div>
  <div class="insta" style="left:926px;top:252px;background:linear-gradient(#2d3d5a,#d09a5a)" role="img" aria-label="Home photo"></div>
  <div class="insta" style="left:986px;top:252px;background:linear-gradient(#6a9fd8,#e2e2e2)" role="img" aria-label="Home photo"></div>
  <div class="copyright">Copyright &copy; 2022 <span>RC</span>. All Right Reserved</div>
</footer>

</body>
</html>
```